Quorvel Business Card

Looking for business card ideas. Company name is Quorvel. Have a few basic ideas on attachment. Please submit anything with the logo and general information from attachment.

Industry/Entity Type

Business

```html
<!DOCTYPE html>
<html lang="en">
<head>
<meta charset="utf-8">
<title>Quorvel Business Card</title>
<link rel="stylesheet" href="https://fonts.googleapis.com/css2?family=Arimo:ital,wght@0,400;1,700&family=Questrial&display=swap">
<style>
  :root {
    --backdrop: #0b0b0d;
    --card: #ffffff;
    --ink: #3d3d3d;
    --ink-soft: #333333;
    --accent-red: #e0201b;
    --accent-orange: #ef6a1a;
    --accent-yellow: #f6c516;
    --rule: #4a4a4a;
  }
  * { box-sizing: border-box; margin: 0; padding: 0; }
  html, body { width: 1200px; height: 999px; overflow: hidden; background: var(--backdrop); }
  .stage { position: relative; width: 1200px; height: 999px; }
  .card {
    position: absolute; top: 154px; width: 458px; height: 689px;
    background: var(--card);
    border-radius: 0 45px 0 45px;
    overflow: hidden;
  }
  .card--classic { left: 99px; }
  .card--pulse { left: 644px; }
  .brand { position: absolute; left: 19px; top: 18px; display: flex; align-items: center; gap: 10px; }
  .brand__dot { width: 48px; height: 48px; border-radius: 50%; background: var(--accent-red); }
  .brand__name {
    font-family: "Questrial", sans-serif; font-size: 30px; color: var(--accent-red);
    letter-spacing: 3px;
  }
  .person { position: absolute; font-family: "Questrial", sans-serif; color: var(--ink); }
  .person__name { font-size: 35px; letter-spacing: 1.5px; line-height: 1; white-space: nowrap; }
  .person__role {
    font-family: "Arimo", sans-serif; font-style: italic; font-weight: 700;
    font-size: 16px; letter-spacing: 12px; color: var(--ink); line-height: 1;
  }
  .card--classic .person { left: 0; width: 458px; top: 222px; text-align: center; }
  .card--classic .person__name {
    display: inline-block; padding: 0 2px 6px; border-bottom: 2px solid var(--rule);
  }
  .card--classic .person__role { margin-top: 6px; margin-right: -12px; }
  .card--pulse .person { right: 32px; top: 230px; text-align: right; }
  .card--pulse .person__role { margin-top: 14px; margin-right: -12px; }
  .pulse-motif {
    position: absolute; left: 44px; top: 192px; width: 76px; height: 122px;
    background: linear-gradient(180deg, rgba(239,106,26,0.18), rgba(224,32,27,0.28));
  }
  .pulse-rule {
    position: absolute; left: 0; top: 265px; width: 458px; height: 4px;
    background: linear-gradient(90deg, var(--accent-red), var(--accent-orange) 35%, var(--accent-yellow));
  }
  .contact {
    position: absolute; left: 41px; top: 456px;
    font-family: "Arimo", sans-serif; font-size: 24px; color: var(--ink-soft);
  }
  .contact__address { line-height: 30px; margin-bottom: 16px; }
  .contact__list { list-style: none; }
  .contact__list li { position: relative; padding-left: 25px; line-height: 32px; }
  .contact__list li::before {
    content: ""; position: absolute; left: 0; top: 12px;
    width: 11px; height: 11px; border-radius: 50%; background: var(--accent-red);
  }
</style>
</head>
<body>
<main class="stage">
  <section class="card card--classic">
    <div class="brand"><span class="brand__dot"></span><span class="brand__name">Quorvel</span></div>
    <div class="person">
      <div class="person__name">DELAN MORROW</div>
      <div class="person__role">DIRECTOR</div>
    </div>
    <div class="contact">
      <p class="contact__address">2840 W. Harlow St.<br>Marlow, TX 79540</p>
      <ul class="contact__list">
        <li>Office: (555) 214-7030</li>
        <li>Cell: (555) 386-9152</li>
        <li>dmorrow@quorvel.com</li>
        <li>www.quorvel.org</li>
      </ul>
    </div>
  </section>

  <section class="card card--pulse">
    <div class="brand"><span class="brand__dot"></span><span class="brand__name">Quorvel</span></div>
    <div class="pulse-motif" role="img" aria-label="Heartbeat pulse motif in red and orange"></div>
    <div class="pulse-rule"></div>
    <div class="person">
      <div class="person__name">DELAN MORROW</div>
      <div class="person__role">DIRECTOR</div>
    </div>
    <div class="contact">
      <p class="contact__address">2840 W. Harlow St.<br>Marlow, TX 79540</p>
      <ul class="contact__list">
        <li>Office: (555) 214-7030</li>
        <li>Cell: (555) 386-9152</li>
        <li>dmorrow@quorvel.com</li>
        <li>www.quorvel.org</li>
      </ul>
    </div>
  </section>
</main>
</body>
</html>
```